Fix Up Brochure for TRK Holdings

Hello,

We have an old structure and content of a brochure we previously sent to prospective/new clients. We would like to update it, make it more pleasant to the eye, and have some of the language cleaned up for a smooth read; more graphics on front and back.

You have the freedom to be creative with the graphic design... Not too edgy, but we do use unique option and hedging strategies that many firms do not. We are trying to convey that we are not your typical financial advisors.

Our business is TRK Holdings, which provides portfolio management to 20-80 year old individuals and small to medium businesses. (Our website is not create YET, but we are working on it right now).

This particular brochure will be given to new/prospective clients, making it a big marketing piece for our business. Attached is a photo of the folder which we have already created for the business, and this brochure (2 fold, not 3) will be inserted inside on thick paper. Therefore, the design of the brochure has to align with the photo attached.

Folder is about 9 x 12, so the brochure is standard 8 1/2 x 11, with about half inch margins. We would like 4 8 1/2 x 11 pages, or 2 17 x 11 landscape pages that we then fold.

All of the content inside the brochure (that we have right now) is also attached in PDF format. Please review/revise if needed.

Within the brochure, please feel free to include any images to do with the financial industry, as long as it's done tastefully.

Also, I have attached a jpeg of our logo. Colors are navy blue going into a royal blue, and lime green.

Conservative wise.. On a scale 1-10 (1 being most conservative) we are about a 6-7.
Updates

Uploaded PDF, a .eps version of the logo, TRK Holdings.

Also included color scheme for the blue & green in the logo

Industry/Entity Type

Financial

Requirements
Must have
• GREEN RGB:
R: 121
G: 199
B: 27

BLUE RGB:
R: 1
G: 19
B: 107

```html
<!DOCTYPE html>
<html lang="en">
<head>
<meta charset="utf-8">
<title>TRK Holdings – Folder Spread</title>
<link href="https://fonts.googleapis.com/css2?family=Cabin:wght@400;500&family=Cinzel:wght@500&display=swap" rel="stylesheet">
<style>
  :root {
    --brand-navy: #01136b;
    --brand-green: #79c71b;
    --ink: #1a1d2b;
    --paper: #ffffff;
    --white: #ffffff;
    --frame: #dfe3ef;
  }
  html, body {
    margin: 0;
    padding: 0;
    width: 1200px;
    height: 776px;
    overflow: hidden;
    background: var(--paper);
  }
  .spread {
    position: relative;
    width: 1200px;
    height: 776px;
    background: var(--paper);
    font-family: "Cabin", sans-serif;
    color: var(--ink);
  }

  /* Front panel */
  .brand-square {
    position: absolute;
    left: 848px;
    top: 60px;
    width: 110px;
    height: 110px;
    background: var(--brand-navy);
  }
  .front-wordmark {
    position: absolute;
    left: 724px;
    width: 360px;
    top: 208px;
    margin: 0;
    text-align: center;
    font-family: "Cinzel", serif;
    font-weight: 500;
    font-size: 29px;
    line-height: 40px;
    letter-spacing: 6px;
    color: var(--brand-navy);
  }
  .photo {
    position: absolute;
    left: 636px;
    top: 299px;
    width: 528px;
    height: 329px;
    border: 3px solid var(--frame);
    box-sizing: border-box;
    background: linear-gradient(120deg, #5e5a5c 0%, #d8c6b4 35%, #eee6dc 60%, #27304a 100%);
    box-shadow: 0 3px 8px rgba(0,0,0,0.35);
  }
  .tagline {
    position: absolute;
    left: 680px;
    width: 434px;
    top: 666px;
    margin: 0;
    text-align: center;
    color: var(--white);
    font-weight: 400;
    font-size: 21px;
    line-height: 32px;
    font-variant: small-caps;
    letter-spacing: 1.4px;
  }

  /* Back panel */
  .back-mark {
    position: absolute;
    left: 87px;
    top: 278px;
    width: 424px;
    display: flex;
    align-items: center;
    gap: 12px;
  }
  .back-mark .rule {
    flex: 1;
    height: 1px;
    background: var(--brand-navy);
  }
  .back-mark .name {
    font-family: "Cinzel", serif;
    font-weight: 500;
    font-size: 11px;
    letter-spacing: 2px;
    color: var(--brand-navy);
    white-space: nowrap;
  }
  .invite {
    position: absolute;
    left: 73px;
    top: 344px;
    width: 460px;
    margin: 0;
    font-size: 11.5px;
    line-height: 16.5px;
    font-variant: small-caps;
    letter-spacing: 0.5px;
  }
  .topics {
    position: absolute;
    left: 73px;
    top: 463px;
    margin: 0;
    padding: 0;
    list-style: none;
    font-size: 11.5px;
    line-height: 16.5px;
    font-variant: small-caps;
    letter-spacing: 0.5px;
  }
  .green-band {
    position: absolute;
    left: 0;
    top: 596px;
    width: 1200px;
    height: 144px;
    background: var(--brand-green);
  }
  .office {
    position: absolute;
    left: 92px;
    width: 400px;
    top: 605px;
    margin: 0;
    text-align: center;
    color: var(--white);
    font-style: normal;
    font-size: 13px;
    line-height: 20.3px;
    font-variant: small-caps;
    letter-spacing: 0.8px;
  }
</style>
</head>
<body>
<main class="spread">
  <div class="green-band"></div>

  <section class="back-panel">
    <div class="back-mark">
      <span class="rule"></span>
      <span class="name">TRK HOLDINGS</span>
      <span class="rule"></span>
    </div>
    <p class="invite">We invite you to contact us. We will help you define your specific goals and a plan toward achieving them. Call today to begin putting TRK Holdings to work for you and your family, or visit www.TRKHoldings.com for detailed information about:</p>
    <ul class="topics">
      <li>- Investment Management</li>
      <li>- Our Investment Philosophy</li>
      <li>- The TRK Holdings team</li>
    </ul>
    <address class="office">
      Main Office:<br>
      400 West Harmon Avenue, Suite 210<br>
      Chicago, IL 60606<br>
      P: 555-010-0148<br>
      info@TRKHoldings.com<br>
      www.TRKHoldings.com
    </address>
  </section>

  <section class="front-panel">
    <div class="brand-square"></div>
    <h1 class="front-wordmark">TRK HOLDINGS</h1>
    <div class="photo" role="img" aria-label="Photo of a smiling young couple shaking hands with a financial advisor across a desk"></div>
    <p class="tagline">Customized Strategies<br>to Meet Your Financial Goals</p>
  </section>
</main>
</body>
</html>
```